Update patient consent forms and contract

Objective
Redesign the existing patient contract information document to create a modern,contempory, and easy-to-understand experience for patients. The updated design should improve readability, accessibility, and overall presentation while maintaining compliance with healthcare and legal requirements.

Key Deliverables

Refreshed visual design and layout
Improved information hierarchy and readability
Modern typography and colour palette aligned with brand guidelines
Clear section headings and navigation
Print-ready and digital versions (PDF)

Include KVE Logo within patient KVE consent to treatment. Ideally this document should be portrait not landscape.
Updates

I would love a front page to be included in the document

```html
<!DOCTYPE html>
<html lang="en">
<head>
<meta charset="utf-8">
<title>Halden Orthodontics – Patient Documents</title>
<link href="https://fonts.googleapis.com/css2?family=Outfit:wght@300;400;500;600;700&display=swap" rel="stylesheet">
<style>
:root{
  --stage:#b7b7b7;
  --paper:#ffffff;
  --blue:#1a8fd6;
  --blue-soft:#d8effb;
  --ink:#1f2d3a;
  --grey-text:#7d848a;
  --footer-grey:#ececec;
}
*{margin:0;padding:0;box-sizing:border-box}
html,body{width:1200px;height:582px;overflow:hidden;background:var(--stage);font-family:"Outfit",sans-serif;color:var(--ink)}
.page{position:absolute;top:86px;width:317px;height:410px;background:var(--paper);overflow:hidden;box-shadow:2px 3px 6px rgba(0,0,0,.18)}
.page--retainer{left:101px}
.page--payment{left:442px}
.page--consent{left:782px}

/* brand lockups */
.brand{display:flex;align-items:center;gap:4px;font-weight:500;white-space:nowrap}
.brand__mark{width:9px;height:9px;border-radius:50%;background:var(--grey-text)}
.brand__mark--square{border-radius:1px;background:var(--blue)}
.brand--kve{color:var(--grey-text)}
.brand--practice{color:var(--blue)}

/* retainer page */
.retainer__head{height:77px;display:flex;align-items:center;justify-content:center;gap:30px;font-size:10px}
.retainer__body{position:absolute;top:77px;left:0;right:0;height:277px;background:var(--blue-soft);padding:12px 20px 0}
.rule-title{display:flex;align-items:center;gap:6px;color:var(--blue);font-weight:600;font-size:12.5px;white-space:nowrap}
.rule-title::before,.rule-title::after{content:"";flex:1;height:.6px;background:var(--blue)}
.retainer__text{margin-top:8px;font-size:6.45px;line-height:11.3px;text-align:justify;font-weight:400}
.retainer__text strong{color:var(--blue);font-weight:600}

/* footer */
.doc-footer{position:absolute;left:0;right:0;bottom:0;height:56px;display:flex;background:var(--footer-grey);font-size:3.9px;line-height:1.35}
.doc-footer__bank{width:102px;background:var(--blue);color:#fff;padding:8px 0 0 18px}
.doc-footer__bank h4,.doc-footer__col h4{font-size:4.6px;font-weight:600;margin-bottom:3px}
.bank-row{display:flex;margin-bottom:4px}
.bank-row span:first-child{width:43px;opacity:.9}
.bank-row span:last-child{font-weight:600}
.doc-footer__col{padding:8px 0 0 10px}
.doc-footer__col--info{width:104px;border-right:.5px solid #c9c9c9;margin-top:6px;padding-top:2px}
.info-row{display:flex;align-items:center;gap:4px;margin-bottom:3.5px}
.info-row svg{width:5px;height:5px;flex:none}
.doc-row{display:flex;gap:4px;margin-bottom:2.4px}
.doc-row svg{width:5px;height:6px;flex:none}
.doc-row b{display:block;font-weight:600}

/* payment page */
.payment__head{position:absolute;top:14px;left:17px;right:14px;display:flex;align-items:center;justify-content:space-between}
.payment__title{font-size:11.2px;font-weight:600}
.payment__brands{display:flex;gap:10px;font-size:6.5px}
.payment__intro{position:absolute;top:38px;left:18px;right:16px;font-size:5.6px;line-height:9.6px}
.payment__intro .thanks{font-weight:600;margin-bottom:5px}
.section-label{position:absolute;left:12px;color:var(--blue);font-weight:600;font-size:8.6px;display:flex;align-items:center;gap:4px}
.section-label::before{content:"";width:2px;height:2px;border-radius:50%;background:var(--blue)}
.payment__options{position:absolute;top:102px;left:0;right:0;height:126px;background:var(--blue-soft);padding:5px 18px 0}
.option{position:relative;font-size:5.5px;line-height:7.4px}
.option__label{display:flex;align-items:center;gap:5px;font-weight:600;font-size:6px;height:11px}
.checkbox{width:10px;height:10px;background:#fff;border:.6px solid var(--blue);border-radius:1.5px}
.option__icon{position:absolute;left:135px;top:4px;width:27px;height:20px}
.option__line{margin-top:4px}
.option__note{margin-top:8px}
.option-divider{border-top:.6px dashed #9fcbe6;margin:7px 0 7px}
.payment__important{position:absolute;top:250px;left:18px;right:30px;font-size:5.5px;line-height:7.4px}
.payment__declaration{position:absolute;top:292px;left:18px;font-size:5.5px}
.sign-line{position:absolute;top:334px;width:53px;border-top:.6px solid var(--ink);text-align:center;font-size:6.2px;font-weight:500;padding-top:2px}

/* consent page */
.consent__left{position:absolute;top:0;left:0;width:159px;height:100%;background:var(--blue-soft);padding:12px 9px 0 10px}
.consent__right{position:absolute;top:0;left:159px;right:0;height:100%;padding:13px 10px 0 5px}
.mini-rule{display:flex;align-items:center;gap:5px;font-size:5.2px;font-weight:600;white-space:nowrap;margin:0 0 2px}
.mini-rule::before,.mini-rule::after{content:"";flex:1;height:.4px;background:var(--ink)}
.mini-rule--blue{color:var(--blue)}
.mini-rule--blue::before,.mini-rule--blue::after{background:var(--blue)}
.fine{font-size:3.1px;line-height:4.55px;text-align:justify;margin-bottom:5px}
.fine-head{font-size:3.9px;font-weight:600;color:var(--blue);margin-bottom:1px}
.consent__brands{display:flex;justify-content:center;gap:14px;font-size:5px;margin:10px 0 6px}
.consent-title{display:flex;align-items:center;gap:6px;color:var(--blue);font-weight:600;font-size:7px;white-space:nowrap;margin-bottom:4px}
.consent-title::before,.consent-title::after{content:"";flex:1;height:.5px;background:var(--blue)}
.consent-field{font-size:5.1px;line-height:6.6px;padding:2px 0 3px 4px;border-bottom:.5px dotted #8fa2b0;position:relative;margin-bottom:2px}
.consent-field::before{content:"";position:absolute;left:0;top:5px;width:1.6px;height:1.6px;border-radius:50%;background:var(--blue)}
</style>
</head>
<body>

<!-- Page 1: retainer policy -->
<section class="page page--retainer">
  <header class="retainer__head">
    <div class="brand brand--kve"><span class="brand__mark"></span>KVE</div>
    <div class="brand brand--practice"><span class="brand__mark brand__mark--square"></span>Halden Orthodontics</div>
  </header>
  <div class="retainer__body">
    <h1 class="rule-title">Our retainer policy</h1>
    <p class="retainer__text">Wearing your retainers is the most important part of your orthodontic journey. Teeth shifting is a part of the natural ageing process just like getting wrinkles, so lifetime maintenance is crucial. Healthy teeth are not meant to be glued together, they are individual units and function independently. This is normally only done for areas of weak bone and gum or damaged teeth. For this reason <strong>WE DO NOT ENCOURAGE THE USE OF ‘BONDED’ OR ‘PERMANENT’ RETAINERS.</strong> Instead we advocate responsible use of removable retainers to maintain your smile. Permanent or bonded retainers are not actually permanent and can cause other unexpected problems after treatment is completed, such as difficulty to clean around those teeth which can cause plaque trapping and lead to localised gum and bone loss. They are subject to breaking frequently, which is the reason that when bonded retainers are placed, it is recommended that you still wear a removable retainer over them anyway. Bonded retainers only hold the front few teeth, whereas your orthodontic treatment involved improvements of ALL your teeth. Thus, holding the front teeth only gives the back teeth a chance to move out of alignment. The retainers we provide at Halden Orthodontics, are only worn at night and will hold ALL your teeth where they are at the end of your orthodontic treatment. Even excellent retainer wear will not guarantee that the teeth will stay exactly the same forever, due to the natural ageing and bone changing processes. Minor alignment adjustments may be made to your retainers in the future to ensure that you remain happy with your smile. After 2 years of retainer reviews, further follow up care may be charged at the current office visit rate. Lost or broken retainers will incur a fee for replacement or repair.</p>
  </div>
  <footer class="doc-footer">
    <div class="doc-footer__bank">
      <h4>Our bank account details:</h4>
      <div class="bank-row"><span>Account Name</span><span>: Halden Orthodontics</span></div>
      <div class="bank-row"><span>Bank</span><span>: Southbank</span></div>
      <div class="bank-row"><span>BSB</span><span>: 012 345</span></div>
      <div class="bank-row"><span>Account Number</span><span>: 10456789</span></div>
    </div>
    <div class="doc-footer__col doc-footer__col--info">
      <h4>Information:</h4>
      <div class="info-row"><svg viewBox="0 0 10 10"><path d="M5 1a3 3 0 0 1 3 3c0 2.5-3 5-3 5S2 6.5 2 4a3 3 0 0 1 3-3z" fill="none" stroke="#1a8fd6"/></svg>48 Larkin St, Ferndale VIC 3000</div>
      <div class="info-row"><svg viewBox="0 0 10 10"><path d="M2 1l2 0 1 2.5-1.2 1a5 5 0 0 0 2.7 2.7l1-1.2L10 7v2c-5 0-8-3-8-8z" fill="none" stroke="#1a8fd6"/></svg>03 5550 1234</div>
      <div class="info-row"><svg viewBox="0 0 10 10"><rect x="1.5" y="2" width="7" height="6.5" fill="none" stroke="#1a8fd6"/><path d="M3 4h4M3 6h4" stroke="#1a8fd6"/></svg>03 5550 5678</div>
      <div class="info-row"><svg viewBox="0 0 10 10"><rect x="1" y="2.5" width="8" height="5.5" fill="none" stroke="#1a8fd6"/><path d="M1 2.5l4 3 4-3" fill="none" stroke="#1a8fd6"/></svg>hello@haldenortho.com.au</div>
    </div>
    <div class="doc-footer__col">
      <h4>Registered Specialist Orthodontists:</h4>
      <div class="doc-row"><svg viewBox="0 0 10 12"><path d="M2 1c2 0 2 1 3 1s1-1 3-1 2 3 1 6-1 4-2 4-1-3-2-3-1 3-2 3-1-1-2-4S0 1 2 1z" fill="none" stroke="#1a8fd6"/></svg><div><b>Dr Mara Ellison</b>MDSc, Grad Dip Clin Dent, BDSc(Hons)</div></div>
      <div class="doc-row"><svg viewBox="0 0 10 12"><path d="M2 1c2 0 2 1 3 1s1-1 3-1 2 3 1 6-1 4-2 4-1-3-2-3-1 3-2 3-1-1-2-4S0 1 2 1z" fill="none" stroke="#1a8fd6"/></svg><div><b>Dr Tom Reyes</b>MDSc, Grad Dip Clin Dent, MOrth, BDSc</div></div>
      <div class="doc-row"><svg viewBox="0 0 10 12"><path d="M2 1c2 0 2 1 3 1s1-1 3-1 2 3 1 6-1 4-2 4-1-3-2-3-1 3-2 3-1-1-2-4S0 1 2 1z" fill="none" stroke="#1a8fd6"/></svg><div><b>Dr Priya Nandan</b>DCD, MOrth, MRACDS (Orth), BDSc (Hons)</div></div>
    </div>
  </footer>
</section>

<!-- Page 2: payment options -->
<section class="page page--payment">
  <header class="payment__head">
    <h1 class="payment__title">Payment Option Selection</h1>
    <div class="payment__brands">
      <div class="brand brand--kve"><span class="brand__mark"></span>KVE</div>
      <div class="brand brand--practice"><span class="brand__mark brand__mark--square"></span>Halden Orthodontics</div>
    </div>
  </header>
  <div class="payment__intro">
    <p class="thanks">Thank you for choosing Halden Orthodontics.</p>
    <p>To assist with managing your treatment fees, please select your preferred payment method below. If you would prefer to pay at each scheduled appointment, please advise our reception team. Please note that appointments are generally scheduled every 6–8 weeks.</p>
  </div>
  <h2 class="section-label" style="top:88px">Please select one option:</h2>
  <div class="payment__options">
    <div class="option">
      <div class="option__label"><span class="checkbox"></span>Credit Card Direct Debit</div>
      <svg class="option__icon" viewBox="0 0 27 20" fill="none" stroke="#1a8fd6" stroke-width=".7"><rect x="1" y="1" width="21" height="14" rx="1.5"/><path d="M1 5h21M4 9h7"/><circle cx="21" cy="15" r="4" fill="#d8effb"/><path d="M19 15h4M22 13.6l1.2 1.4-1.2 1.4"/></svg>
      <p class="option__line">I would like to pay via credit card direct debit.</p>
      <p class="option__note">I understand that Halden Orthodontics will send me a secure PayLink payment link to enter my credit card details. The card provided will be securely stored and used as my nominated payment method for future scheduled payments relating to my treatment plan.</p>
    </div>
    <div class="option-divider"></div>
    <div class="option">
      <div class="option__label"><span class="checkbox"></span>Monthly Direct Bank Transfer</div>
      <svg class="option__icon" viewBox="0 0 27 20" fill="none" stroke="#1a8fd6" stroke-width=".7" style="left:130px"><rect x="2" y="2" width="19" height="17" rx="2"/><path d="M2 6h19M7 0.5v3M16 0.5v3M7 10h9l-2-1.5M16 14H7l2 1.5"/></svg>
      <p class="option__line">I would like to pay via monthly direct bank transfer.</p>
      <p class="option__note">I understand that I am responsible for ensuring monthly payments are made on time in accordance with my agreed payment arrangement.</p>
    </div>
  </div>
  <h2 class="section-label" style="top:235px">Important</h2>
  <p class="payment__important">When making direct transfer payments, please use the <b>patient’s full name</b> as the payment reference (for example: Jane Carter), rather than the account holder’s name. This ensures payments are correctly allocated to your treatment account.</p>
  <h2 class="section-label" style="top:277px">Patient Declaration</h2>
  <p class="payment__declaration">I have read and understood the payment options above and agree to my selected payment method.</p>
  <div class="sign-line" style="left:49px">Signature</div>
  <div class="sign-line" style="left:215px">Date</div>
  <footer class="doc-footer">
    <div class="doc-footer__bank">
      <h4>Our bank account details:</h4>
      <div class="bank-row"><span>Account Name</span><span>: Halden Orthodontics</span></div>
      <div class="bank-row"><span>Bank</span><span>: Southbank</span></div>
      <div class="bank-row"><span>BSB</span><span>: 012 345</span></div>
      <div class="bank-row"><span>Account Number</span><span>: 10456789</span></div>
    </div>
    <div class="doc-footer__col doc-footer__col--info">
      <h4>Information:</h4>
      <div class="info-row"><svg viewBox="0 0 10 10"><path d="M5 1a3 3 0 0 1 3 3c0 2.5-3 5-3 5S2 6.5 2 4a3 3 0 0 1 3-3z" fill="none" stroke="#1a8fd6"/></svg>48 Larkin St, Ferndale VIC 3000</div>
      <div class="info-row"><svg viewBox="0 0 10 10"><path d="M2 1l2 0 1 2.5-1.2 1a5 5 0 0 0 2.7 2.7l1-1.2L10 7v2c-5 0-8-3-8-8z" fill="none" stroke="#1a8fd6"/></svg>03 5550 1234</div>
      <div class="info-row"><svg viewBox="0 0 10 10"><rect x="1.5" y="2" width="7" height="6.5" fill="none" stroke="#1a8fd6"/><path d="M3 4h4M3 6h4" stroke="#1a8fd6"/></svg>03 5550 5678</div>
      <div class="info-row"><svg viewBox="0 0 10 10"><rect x="1" y="2.5" width="8" height="5.5" fill="none" stroke="#1a8fd6"/><path d="M1 2.5l4 3 4-3" fill="none" stroke="#1a8fd6"/></svg>hello@haldenortho.com.au</div>
    </div>
    <div class="doc-footer__col">
      <h4>Registered Specialist Orthodontists:</h4>
      <div class="doc-row"><svg viewBox="0 0 10 12"><path d="M2 1c2 0 2 1 3 1s1-1 3-1 2 3 1 6-1 4-2 4-1-3-2-3-1 3-2 3-1-1-2-4S0 1 2 1z" fill="none" stroke="#1a8fd6"/></svg><div><b>Dr Mara Ellison</b>MDSc, Grad Dip Clin Dent, BDSc(Hons)</div></div>
      <div class="doc-row"><svg viewBox="0 0 10 12"><path d="M2 1c2 0 2 1 3 1s1-1 3-1 2 3 1 6-1 4-2 4-1-3-2-3-1 3-2 3-1-1-2-4S0 1 2 1z" fill="none" stroke="#1a8fd6"/></svg><div><b>Dr Tom Reyes</b>MDSc, Grad Dip Clin Dent, MOrth, BDSc</div></div>
      <div class="doc-row"><svg viewBox="0 0 10 12"><path d="M2 1c2 0 2 1 3 1s1-1 3-1 2 3 1 6-1 4-2 4-1-3-2-3-1 3-2 3-1-1-2-4S0 1 2 1z" fill="none" stroke="#1a8fd6"/></svg><div><b>Dr Priya Nandan</b>DCD, MOrth, MRACDS (Orth), BDSc (Hons)</div></div>
    </div>
  </footer>
</section>

<!-- Page 3: treatment information and consent -->
<section class="page page--consent">
  <div class="consent__left">
    <h2 class="mini-rule">ORTHODONTIC TREATMENT</h2>
    <p class="fine">Orthodontic treatment promotes a healthy smile, healthier teeth and gums and a better bite for normal chewing. Results depend on the understanding and co-operation of the patient. This form covers the usual risks and limitations of treatment. Alternative options may exist and you may ask your orthodontist to explain anything you do not understand. While treatment has clear benefits, it also has limitations and potential risks. Keep in mind that results cannot be guaranteed, as the response of the patient is an unknown factor in any correction. Please ask if you have any questions at any stage of your care.</p>
    <h2 class="mini-rule">BENEFITS</h2>
    <p class="fine">Orthodontics plays an important role in improving overall oral health and achieving balance between the face and teeth. A correct bite works in harmony with the jaw joints and muscles, providing comfortable chewing. Properly aligned teeth are easier to brush and clean, so the likelihood of decay and gum disease may be reduced. Aligned teeth are also less likely to suffer abnormal wear. Because of individual conditions, not every benefit may be attainable for every patient.</p>
    <h2 class="mini-rule mini-rule--blue">RISKS</h2>
    <p class="fine">All forms of medical and dental treatment have some risk and limitations. Fortunately, complications in orthodontics are infrequent and usually of minor consequence. They should still be considered when deciding to undergo treatment. The principal risks are listed below.</p>
    <h3 class="fine-head">1. Oral Hygiene</h3>
    <p class="fine">Appliances do not cause decay, but tooth decay, gum disease and permanent marks can occur if patients eat sugary food or do not brush thoroughly. These problems can also occur without treatment, yet the risk rises while braces are worn, so extra care is needed.</p>
    <h3 class="fine-head">2. Relapse</h3>
    <p class="fine">Teeth may tend to change position after treatment. Faithful retainer wear reduces this tendency. Teeth can move at any time of life, whether or not treatment was carried out, and changes in late teen growth, wisdom teeth, breathing or habits may alter the result. Occasionally movement is enough to need a further short course of treatment.</p>
    <h3 class="fine-head">3. Periodontal Health</h3>
    <p class="fine">The bone and gums supporting the teeth may be affected during treatment if a condition already exists. In general, treatment lessens the chance of gum problems, but loss of supporting bone can occur if plaque is not removed daily with good oral hygiene.</p>
    <h3 class="fine-head">4. Root Shortening</h3>
    <p class="fine">In some patients the roots of teeth may shorten during treatment. It is nearly impossible to predict who is prone. Usually this does not cause significant problems, but on rare occasions it may affect the long term health of the teeth involved.</p>
    <h3 class="fine-head">5. Jaw Joints</h3>
    <p class="fine">Occasionally patients may have pain or dysfunction in the jaw joints, felt as joint pain, headaches or ear problems. These may occur with or without treatment and should be reported to the orthodontist. Symptoms may last from a few days to several weeks.</p>
    <h3 class="fine-head">6. Tooth Vitality</h3>
    <p class="fine">A tooth traumatised by an earlier accident or with large fillings may have damaged nerves. Tooth movement can sometimes aggravate this, leading to discolouration or the need for root canal treatment to restore the tooth.</p>
  </div>
  <div class="consent__right">
    <h3 class="fine-head">7. Loose appliances and discomfort</h3>
    <p class="fine">Cheeks, lips and gums may be scratched or irritated by new or loose appliances. Very rarely parts may be swallowed or inhaled. Inform your orthodontist of any unusual symptoms or broken parts as soon as they are noticed. Tenderness after adjustments usually lasts 24 to 48 hours.</p>
    <h3 class="fine-head">8. Atypical Growth</h3>
    <p class="fine">Insufficient, excessive or uneven growth of the jaws may limit the ability to achieve the desired result. If growth becomes disproportionate, treatment may be prolonged or require further care. In some cases jaw surgery may be needed to achieve the best possible result.</p>
    <h3 class="fine-head">9. Headgear</h3>
    <p class="fine">If improperly handled, headgear may cause injury to the face. Patients are warned not to wear it during boisterous or competitive activity.</p>
    <h3 class="fine-head">10. Treatment Time</h3>
    <p class="fine">Total treatment time may exceed the estimate. Poor wear of appliances or elastics, poor oral hygiene, broken appliances and missed appointments can lengthen treatment and affect the quality of results.</p>
    <h3 class="fine-head">11. Co-operation</h3>
    <p class="fine">Co-operation throughout treatment is your best guarantee of a pleasing smile and good bite. Failure to co-operate may force a change in goals, and as a last resort treatment may be suspended.</p>
    <h3 class="fine-head">12. Ceramic Brackets</h3>
    <p class="fine">Where ceramic brackets are used, some patients have reported bracket breakage or damage to teeth, including wear of enamel or chipping when brackets are removed. Fragments may be harmful if chewed or swallowed.</p>
    <h3 class="fine-head">13. Complementary aesthetic dentistry</h3>
    <p class="fine">If your teeth vary from normal size or shape, further restorative treatment such as bonding, crowns or gum therapy may be needed for the ideal result.</p>
    <h3 class="fine-head">14. General Health</h3>
    <p class="fine">General medical problems can affect treatment. Please keep your orthodontist informed of any changes to your medical health.</p>
    <div class="consent__brands">
      <div class="brand brand--kve"><span class="brand__mark" style="width:6px;height:6px"></span>KVE</div>
      <div class="brand brand--practice"><span class="brand__mark brand__mark--square" style="width:6px;height:6px"></span>Halden Orthodontics</div>
    </div>
    <h2 class="consent-title">CONSENT TO TREATMENT</h2>
    <div class="consent-field">I here by authorize:</div>
    <div class="consent-field">To carry out orthodontic treatment and any other related procedures deemed necessary including X-rays, for the welfare and treatment of:</div>
    <div class="consent-field">Signature of patient or parent/guardian:</div>
    <div class="consent-field">Name :</div>
    <div class="consent-field">Relationship to patient :</div>
    <div class="consent-field">Date :</div>
    <div class="consent-field">Signature of Orthodontis :</div>
  </div>
</section>

</body>
</html>
```